I need a professional business card to handout at networking events for my senior helper business. I would like to use the logo I have uploaded. The design should be clear and easy to read and should list the following information...
Dessa Quillan
Owner
www.BrightwayElderAssist.example
Quillport, Texas
555.304.2291
Dessa@brightwayelderassist.example

Target Market(s)

Senior Citizens

Industry/Entity Type

Personal Helper/ Assisstant

Contact Information for Business Card

I have included the details in the project description box.

Font styles to use
Serif

Colors
0054AA
0677BA
7BADD7
CADEEF
E8F1F8
59FF00
82FF00
B8FF75
E3FFCB
F4FFEA
E54698
E96AAD
F1A4CE
F9D9EA
FCEFF6
6B429C
8869AF
B7A5CE
E3DAEB
F3F0F8

Requirements
Must have
• Include uploaded logo
Nice to have
• The log that has been uploaded
Should not have
• No crazy fonts

```html
<!DOCTYPE html>
<html lang="en">
<head>
<meta charset="utf-8">
<title>Brightway Elder Assist – Business Card</title>
<link rel="stylesheet" href="https://fonts.googleapis.com/css2?family=Montserrat:wght@500;600;700&family=Questrial&display=swap">
<style>
  :root {
    --page-bg: #f1f1f3;
    --card-white: #ffffff;
    --brand-purple: #5d4ea3;
    --photo-purple-top: #574b8d;
    --photo-purple-bottom: #3f3775;
    --brand-pink: #dc2a63;
    --text-white: #ffffff;
  }
  * { margin: 0; padding: 0; box-sizing: border-box; }
  html, body {
    width: 1200px; height: 1200px; overflow: hidden;
    background: var(--page-bg);
  }
  .canvas { position: relative; width: 1200px; height: 1200px; }

  .card {
    position: absolute; left: 410px; width: 681px; height: 396px;
    border-radius: 26px; overflow: hidden;
    box-shadow: 0 4px 14px rgba(0,0,0,0.10);
  }
  .card-front { top: 197px; }
  .card-back { top: 671px; background: var(--card-white); }

  /* Front */
  .front-photo {
    position: absolute; inset: 0;
    background: linear-gradient(135deg, var(--photo-purple-top) 0%, #4c4383 55%, var(--photo-purple-bottom) 100%);
  }
  .front-brand {
    position: absolute; left: 338px; top: 114px;
    font-family: "Questrial", sans-serif; color: var(--text-white);
    line-height: 1;
  }
  .front-brand .brand-main { display: block; font-size: 52px; letter-spacing: 0.5px; }
  .front-brand .brand-sub { display: block; font-size: 28px; margin-top: 4px; letter-spacing: 0.5px; }

  /* Back */
  .contact {
    position: absolute; left: 56px; top: 98px;
    font-family: "Montserrat", sans-serif; color: var(--brand-purple);
  }
  .contact-name { font-size: 20px; font-weight: 600; letter-spacing: 0.2px; line-height: 26px; }
  .contact-phone { font-size: 45px; font-weight: 700; letter-spacing: -1.5px; line-height: 50px; margin-top: 2px; }
  .contact-line, .contact-city { font-size: 15.5px; font-weight: 600; line-height: 22px; }

  .back-brand {
    position: absolute; left: 46px; top: 278px;
    display: flex; align-items: center; gap: 12px;
    font-family: "Questrial", sans-serif; color: var(--brand-purple);
  }
  .back-brand .brand-dot {
    width: 54px; height: 54px; border-radius: 50%; background: var(--brand-pink);
  }
  .back-brand .brand-text { line-height: 1; }
  .back-brand .brand-main { display: block; font-size: 42px; }
  .back-brand .brand-sub { display: block; font-size: 24px; margin-top: 3px; }

  .back-mark {
    position: absolute; left: 420px; top: 140px; width: 250px;
    font-family: "Questrial", sans-serif; color: var(--brand-pink);
    text-align: center; line-height: 1.05;
  }
  .back-mark .brand-main { display: block; font-size: 48px; }
  .back-mark .brand-sub { display: block; font-size: 30px; margin-top: 6px; }

  .social {
    position: absolute; left: 448px; top: 326px;
    display: flex; align-items: center; gap: 10px;
    font-family: "Montserrat", sans-serif; color: var(--brand-purple);
    font-size: 18px; font-weight: 500;
  }
  .social-label { margin-right: 2px; }
  .social-dot { width: 27px; height: 27px; border-radius: 50%; background: var(--brand-purple); }
</style>
</head>
<body>
<main class="canvas">

  <section class="card card-front">
    <div class="front-photo" role="img" aria-label="Photo of two smiling seniors giving each other a high five at a table, tinted purple"></div>
    <div class="front-brand">
      <span class="brand-main">Brightway</span>
      <span class="brand-sub">Elder Assist</span>
    </div>
  </section>

  <section class="card card-back">
    <div class="contact">
      <p class="contact-name">DESSA QUILLAN | OWNER</p>
      <p class="contact-phone">555.304.2291</p>
      <p class="contact-line">Dessa@brightwayelderassist.example</p>
      <p class="contact-line">www.BrightwayElderAssist.example</p>
      <p class="contact-city">QUILLPORT, TEXAS</p>
    </div>

    <div class="back-brand">
      <span class="brand-dot"></span>
      <span class="brand-text">
        <span class="brand-main">Brightway</span>
        <span class="brand-sub">Elder Assist</span>
      </span>
    </div>

    <div class="back-mark">
      <span class="brand-main">Brightway</span>
      <span class="brand-sub">Elder Assist</span>
    </div>

    <div class="social">
      <span class="social-label">Find us on:</span>
      <span class="social-dot" aria-hidden="true"></span>
      <span class="social-dot" aria-hidden="true"></span>
      <span class="social-dot" aria-hidden="true"></span>
    </div>
  </section>

</main>
</body>
</html>
```